Kestrova Physical Therapy Website

I would need a clean modern website built to showcase my Physical therapy brand and services. I would need a simple but descriptive website that can ultimately connect my patients to my electronic medical portal so they may book an appointment..

```html
<!DOCTYPE html>
<html lang="en">
<head>
<meta charset="utf-8">
<title>Kestrova Physical Therapy &amp; Wellness</title>
<link rel="stylesheet" href="https://fonts.googleapis.com/css2?family=Raleway:ital,wght@0,300;0,400;0,500;0,600;0,700;1,400&family=Open+Sans:ital,wght@0,400;0,600;0,700;1,400&display=swap">
<style>
:root{
  --teal:#13857e;
  --teal-dark:#0f716b;
  --green:#7cc242;
  --blue:#3f55a5;
  --ink:#2b2b2b;
  --muted:#555;
  --light:#eef2f3;
  --white:#fff;
}
*{box-sizing:border-box;margin:0;padding:0}
html,body{width:1200px;height:5026px;overflow:hidden}
body{position:relative;font-family:"Open Sans",sans-serif;color:var(--ink);background:var(--white)}
.abs{position:absolute}
.bands{position:absolute;left:0;top:0;width:1200px;height:5026px}
.topbar{left:0;top:0;width:1200px;height:43px;background:var(--teal);color:#fff;font-size:12px}
.topbar .contact{left:72px;top:13px;display:flex;gap:28px;align-items:center}
.topbar .contact span{display:flex;align-items:center;gap:6px}
.topbar .social{right:72px;top:12px;display:flex;gap:16px}
.topbar .social i{display:block;width:16px;height:16px;border-radius:50%;background:#fff;opacity:.9}
.hero-photo{left:0;top:43px;width:1200px;height:650px;background:linear-gradient(90deg,#f3f5f6 0%,#eef1f3 45%,#d9dfe2 60%,#c9d2d6 80%,#e4e9eb 100%)}
.logo{display:flex;align-items:center;gap:8px;font-family:"Raleway",sans-serif;font-weight:700;color:var(--teal);font-size:28px;letter-spacing:1px}
.logo i{display:block;width:26px;height:26px;border-radius:50%;background:var(--green)}
.nav{left:451px;top:77px;display:flex;gap:0;font-size:13px;color:var(--ink)}
.nav a{position:absolute;white-space:nowrap;text-decoration:none;color:var(--ink)}
.nav a.active{color:var(--teal)}
.btn{display:flex;align-items:center;justify-content:center;background:var(--green);color:#fff;border-radius:24px;font-size:13px;font-weight:600;text-decoration:none}
.eyebrow{font-family:"Raleway",sans-serif;font-style:italic;font-weight:500;color:var(--teal);font-size:20px}
.h-hero{font-family:"Raleway",sans-serif;font-size:48px;line-height:60px;color:var(--ink)}
.h-hero b{font-weight:700}
.pill{display:flex;align-items:center;justify-content:center;border-radius:16px;font-size:12px;font-weight:600;letter-spacing:1px}
.pill.light{background:#d5ecea;color:var(--teal)}
.pill.dark{background:rgba(255,255,255,.22);color:#fff}
.h-sec{font-family:"Raleway",sans-serif;font-weight:400;font-size:40px;line-height:48px}
.para{font-size:13.5px;line-height:24px;color:var(--muted)}
.ph{display:block}
.svc-item{width:320px}
.svc-icon{width:78px;height:78px;border-radius:14px 14px 14px 40px;background:var(--green);display:flex;align-items:center;justify-content:center}
.svc-title{font-family:"Raleway",sans-serif;font-size:21px;color:#fff;margin-bottom:8px}
.svc-desc{font-size:13.5px;line-height:22px;color:#d8eeec}
.more{font-size:12px;font-weight:600;color:var(--green);margin-top:8px;display:flex;align-items:center;gap:6px}
.more i{display:inline-block;width:11px;height:11px;border-radius:50%;background:var(--green)}
.why-card{width:276px;height:142px;border-radius:20px;background:#fff;box-shadow:0 4px 14px rgba(0,0,0,.12);border-left:3px solid #d9def0}
.why-card .ic{left:10px;top:10px;width:40px;height:40px;border-radius:8px}
.why-card h4{left:78px;top:28px;font-family:"Raleway",sans-serif;font-weight:500;font-size:16px}
.why-card p{left:78px;top:54px;width:180px;font-size:13px;line-height:21px;color:var(--muted)}
.form{left:700px;top:2172px;width:420px;height:554px;background:var(--blue);border-radius:4px}
.form h3{left:26px;top:32px;font-family:"Raleway",sans-serif;font-weight:400;font-size:30px;color:#fff}
.field{height:43px;background:#fff;border:1px solid #cfd5e6;font-size:13px;color:#333;display:flex;align-items:center;padding-left:12px}
.field .caret{position:absolute;right:0;top:0;width:50px;height:41px;border-left:1px solid #cfd5e6;display:flex;align-items:center;justify-content:center}
.team-card{width:234px;height:254px;border-radius:40px 6px 40px 6px;background:linear-gradient(180deg,#c9b8a6,#8d7b6b)}
.team-name{width:234px;text-align:center;color:#fff;font-family:"Raleway",sans-serif;font-weight:700;font-size:18px}
.team-role{width:234px;text-align:center;color:#dfe4f3;font-size:11px;font-style:italic}
.arrow{width:32px;height:32px;border-radius:50%;display:flex;align-items:center;justify-content:center}
.quote{width:330px}
.quote .mark{font-family:"Raleway",sans-serif;font-size:50px;color:var(--teal);line-height:40px;position:absolute;left:0;top:-8px}
.quote p{padding-left:40px;font-size:13.5px;font-style:italic;line-height:24px;color:var(--muted)}
.quote .who{display:flex;align-items:center;gap:12px;margin-top:24px}
.quote .av{width:52px;height:52px;border-radius:50%;background:linear-gradient(135deg,#c6a58c,#6c5446)}
.quote .who b{display:block;color:var(--teal);font-size:14px;font-weight:600}
.quote .who small{font-size:12px;font-style:italic;color:#888}
.blog-card{width:338px;height:406px;background:#fff;border-radius:10px;overflow:hidden}
.blog-card .img{height:211px}
.blog-card .date{left:22px;top:232px;font-size:11px;color:#555;display:flex;gap:6px;align-items:center}
.blog-card .date i{display:block;width:10px;height:10px;background:var(--teal);border-radius:2px}
.blog-card h4{left:22px;top:252px;font-family:"Raleway",sans-serif;font-weight:500;font-size:19px}
.blog-card p{left:22px;top:292px;width:296px;font-size:13px;line-height:20px;color:var(--muted)}
.blog-card .more{position:absolute;left:22px;top:370px;color:#e0463c}
.blog-card .more i{background:#e0463c}
.foot-col h5{font-family:"Raleway",sans-serif;font-weight:600;font-size:15px;margin-bottom:22px}
.foot-col a{display:block;font-size:12.5px;color:var(--muted);text-decoration:none;height:38px}
.hours{font-size:12.5px;color:var(--muted)}
.hours td{height:44px;padding-right:0;vertical-align:top}
.bottombar{left:0;top:4971px;width:1200px;height:55px;background:var(--teal);color:#fff;font-size:11.5px}
</style>
</head>
<body>

<svg class="bands" viewBox="0 0 1200 5026" aria-hidden="true">
  <path d="M0 1347 Q600 1247 1200 1347 L1200 2097 Q600 1963 0 2097 Z" fill="#13857e"/>
  <path d="M0 2888 Q600 2752 1200 2888 L1200 3500 Q600 3380 0 3500 Z" fill="#3f55a5"/>
  <path d="M0 4000 Q600 3920 1200 4000 L1200 4650 Q600 4570 0 4650 Z" fill="#13857e"/>
</svg>

<!-- Top bar -->
<div class="abs topbar">
  <div class="abs contact">
    <span><svg width="12" height="10" viewBox="0 0 12 10"><rect x="0.5" y="0.5" width="11" height="9" fill="none" stroke="#fff"/><path d="M0.5 0.5 L6 5 L11.5 0.5" fill="none" stroke="#fff"/></svg>info@kestrovatherapy.com</span>
    <span><svg width="11" height="11" viewBox="0 0 11 11"><path d="M2 0.5 L4 3 L3 4.5 Q4.5 7 6.5 8 L8 7 L10.5 9 L9 10.5 Q4 10 0.5 2 Z" fill="#fff"/></svg>+01 555 204 318</span>
  </div>
  <div class="abs social"><i></i><i></i><i></i><i></i></div>
</div>

<!-- Hero -->
<div class="abs hero-photo" role="img" aria-label="Physical therapist stretching a patient's neck in a bright clinic room"></div>
<svg class="abs" style="left:0;top:560px" width="1200" height="135" viewBox="0 0 1200 135" aria-hidden="true"><path d="M0 135 L0 132 Q600 -10 1200 132 L1200 135 Z" fill="#fff"/></svg>
<div class="abs logo" style="left:72px;top:86px"><i></i>KESTROVA</div>
<nav class="abs nav" style="left:0;top:77px">
  <a class="active" style="left:451px">Home</a>
  <a style="left:545px">About Us</a>
  <a style="left:660px">Services</a>
  <a style="left:769px">Blog</a>
  <a style="left:855px">Contact Us</a>
</nav>
<a class="abs btn" style="left:954px;top:60px;width:174px;height:47px">Book Appointment</a>
<div class="abs eyebrow" style="left:74px;top:242px">Get your Lifestyle Back <span style="display:inline-block;width:110px;border-top:1px solid var(--teal);vertical-align:middle"></span></div>
<h1 class="abs h-hero" style="left:76px;top:284px;font-weight:400">We Offer Highly<br><b>Specialized Therapy</b></h1>
<a class="abs btn" style="left:72px;top:431px;width:150px;height:43px">Know More</a>
<div class="abs arrow" style="left:575px;top:598px;width:48px;height:48px;background:var(--blue)"><svg width="16" height="10" viewBox="0 0 16 10"><path d="M1 1 L8 8 L15 1" fill="none" stroke="#fff" stroke-width="2"/></svg></div>

<!-- About -->
<div class="abs ph" role="img" aria-label="Therapist treating a patient's back inside a circular frame with a spine illustration" style="left:98px;top:683px;width:440px;height:605px;background:radial-gradient(circle at 58% 28%,#e6e6e6 0,#c9c9c9 34%,#fff 35%,#fff 100%)"></div>
<div class="abs pill light" style="left:611px;top:761px;width:121px;height:31px">ABOUT US</div>
<h2 class="abs h-sec" style="left:611px;top:806px;width:560px">Kestrova Physical Therapy<br>&amp; Wellness</h2>
<p class="abs para" style="left:611px;top:913px;width:520px">Lorem ipsum dolor sit amet, consectetur adipiscing elit, sed do eiusmod tempor incididunt ut labore et dolore magna aliqua. Quis ipsum suspendisse ultrices gravida. Risus commodo viverra maecenas accumsan lacus vel facilisis. Vestibulum blandit risus ac commodo ornare. Ut et bibendum purus, a facilisis lectus. Nulla varius, dolor vitae varius tempor, nibh tortor viverra ex, et faucibus elit ligula vel arcu. Sed laoreet odio ac ipsum vulputate accusan. Duis placerat sapien dapibus malesuada commodo.</p>
<a class="abs btn" style="left:611px;top:1108px;width:150px;height:45px">Read More</a>

<!-- Services -->
<div class="abs pill dark" style="left:70px;top:1389px;width:119px;height:31px">SERVICES</div>
<h2 class="abs h-sec" style="left:70px;top:1435px;color:#fff">Physical Therapy<br>Services</h2>

<div class="abs" style="left:70px;top:1570px">
  <div class="abs svc-icon" style="left:0;top:0"><svg width="40" height="40" viewBox="0 0 40 40" fill="none" stroke="#fff" stroke-width="2"><circle cx="20" cy="20" r="14"/><path d="M20 12 V28 M12 20 H28"/></svg></div>
  <div class="abs svc-item" style="left:90px;top:0"><div class="svc-title">Physical Therapy</div><div class="svc-desc">Sed laoreet odio ac ip vulputate<br>accusan. Duis placerat sapien</div><div class="more">Read More <i></i></div></div>
</div>
<div class="abs" style="left:405px;top:1570px">
  <div class="abs svc-icon" style="left:0;top:0"><svg width="40" height="40" viewBox="0 0 40 40" fill="none" stroke="#fff" stroke-width="2"><circle cx="20" cy="20" r="14"/><path d="M20 12 V28 M12 20 H28"/></svg></div>
  <div class="abs svc-item" style="left:90px;top:0"><div class="svc-title">Massage Therapy</div><div class="svc-desc">Sed laoreet odio ac ip vulputate<br>accusan. Duis placerat sapien</div><div class="more">Read More <i></i></div></div>
</div>
<div class="abs" style="left:70px;top:1715px">
  <div class="abs svc-icon" style="left:0;top:0"><svg width="40" height="40" viewBox="0 0 40 40" fill="none" stroke="#fff" stroke-width="2"><circle cx="20" cy="20" r="14"/><path d="M20 12 V28 M12 20 H28"/></svg></div>
  <div class="abs svc-item" style="left:90px;top:0"><div class="svc-title">Chirpractic Thrapy</div><div class="svc-desc">Sed laoreet odio ac ip vulputate<br>accusan. Duis placerat sapien</div><div class="more">Read More <i></i></div></div>
</div>
<div class="abs" style="left:405px;top:1715px">
  <div class="abs svc-icon" style="left:0;top:0"><svg width="40" height="40" viewBox="0 0 40 40" fill="none" stroke="#fff" stroke-width="2"><circle cx="20" cy="20" r="14"/><path d="M20 12 V28 M12 20 H28"/></svg></div>
  <div class="abs svc-item" style="left:90px;top:0"><div class="svc-title">Work Injuries</div><div class="svc-desc">Sed laoreet odio ac ip vulputate<br>accusan. Duis placerat sapien</div><div class="more">Read More <i></i></div></div>
</div>
<div class="abs" style="left:70px;top:1865px">
  <div class="abs svc-icon" style="left:0;top:0"><svg width="40" height="40" viewBox="0 0 40 40" fill="none" stroke="#fff" stroke-width="2"><circle cx="20" cy="20" r="14"/><path d="M20 12 V28 M12 20 H28"/></svg></div>
  <div class="abs svc-item" style="left:90px;top:0"><div class="svc-title">Sport Injuries</div><div class="svc-desc">Sed laoreet odio ac ip vulputate<br>accusan. Duis placerat sapien</div><div class="more">Read More <i></i></div></div>
</div>
<div class="abs" style="left:405px;top:1865px">
  <div class="abs svc-icon" style="left:0;top:0"><svg width="40" height="40" viewBox="0 0 40 40" fill="none" stroke="#fff" stroke-width="2"><circle cx="20" cy="20" r="14"/><path d="M20 12 V28 M12 20 H28"/></svg></div>
  <div class="abs svc-item" style="left:90px;top:0"><div class="svc-title">Other Therapy</div><div class="svc-desc">Sed laoreet odio ac ip vulputate<br>accusan. Duis placerat sapien</div><div class="more">Read More <i></i></div></div>
</div>

<svg class="abs" style="left:718px;top:1455px" width="420" height="500" viewBox="0 0 420 500" aria-hidden="true"><path d="M4 495 L4 200 Q4 4 200 4 Q320 4 360 90" fill="none" stroke="#7cc242" stroke-width="2"/></svg>
<div class="abs ph" role="img" aria-label="Masked therapist examining a smiling patient's shoulder" style="left:734px;top:1490px;width:392px;height:481px;border-radius:196px 196px 0 0;background:linear-gradient(180deg,#f4f4f4,#dcdfe2 60%,#c8ccd0)"></div>

<!-- Why choose -->
<h2 class="abs h-sec" style="left:72px;top:2205px">Why Choose Us</h2>
<p class="abs para" style="left:72px;top:2262px;width:520px;line-height:24px">Risus commodo viverra maecenas accumsan las vel facilisis. Vestibulum blandit risus ac commodo ornare. Ut et bibendum purus, a facilisis lectus. Nulla varius, dolor vitae varius tempor, nibh tortor viverra ex, et faucibus elit ligula vel arcu.</p>

<div class="abs why-card" style="left:72px;top:2365px"><div class="abs ic" style="background:#3f55a5"></div><h4 class="abs">Personalized Treatment</h4><p class="abs">A facilisis lectus. Nulla varius, dolor vitae varius tempor</p></div>
<div class="abs why-card" style="left:373px;top:2365px"><div class="abs ic" style="background:#f28a5c"></div><h4 class="abs">Experience Staff</h4><p class="abs">A facilisis lectus. Nulla varius, dolor vitae varius tempor</p></div>
<div class="abs why-card" style="left:72px;top:2540px"><div class="abs ic" style="background:#4a7bd1"></div><h4 class="abs">Comfortable Clinic</h4><p class="abs">A facilisis lectus. Nulla varius, dolor vitae varius tempor</p></div>
<div class="abs why-card" style="left:373px;top:2540px"><div class="abs ic" style="background:#3f55a5"></div><h4 class="abs">Therapy Goals</h4><p class="abs">A facilisis lectus. Nulla varius, dolor vitae varius tempor</p></div>

<form class="abs form">
  <h3 class="abs">Fix an Appointment</h3>
  <div class="abs field" style="left:24px;top:91px;width:374px">Name</div>
  <div class="abs field" style="left:24px;top:150px;width:374px">Phone</div>
  <div class="abs field" style="left:24px;top:208px;width:374px">Type Of Service<span class="caret"><svg width="10" height="6"><path d="M0 0 L10 0 L5 6 Z" fill="#666"/></svg></span></div>
  <div class="abs field" style="left:24px;top:269px;width:374px">Staff<span class="caret"><svg width="10" height="6"><path d="M0 0 L10 0 L5 6 Z" fill="#666"/></svg></span></div>
  <div class="abs field" style="left:24px;top:327px;width:374px">MM/DD/YYYY<span class="caret" style="border:0"><svg width="12" height="12" viewBox="0 0 12 12"><rect x="0.5" y="1.5" width="11" height="10" fill="none" stroke="#666"/><path d="M0.5 4.5 H11.5" stroke="#666"/></svg></span></div>
  <div class="abs field" style="left:24px;top:392px;width:183px">From<span class="caret"><svg width="10" height="6"><path d="M0 0 L10 0 L5 6 Z" fill="#666"/></svg></span></div>
  <div class="abs field" style="left:215px;top:392px;width:183px">To<span class="caret"><svg width="10" height="6"><path d="M0 0 L10 0 L5 6 Z" fill="#666"/></svg></span></div>
  <div class="abs btn" style="left:24px;top:456px;width:374px;height:49px;font-size:14px">Check Availability</div>
</form>

<!-- Team -->
<div class="abs pill dark" style="left:540px;top:2897px;width:120px;height:30px">TEAM</div>
<h2 class="abs h-sec" style="left:0;top:2942px;width:1200px;text-align:center;color:#fff">Meet the Team</h2>
<div class="abs team-card" role="img" aria-label="Portrait of physical therapist Marcus Hale" style="left:72px;top:3034px"></div>
<div class="abs team-card" role="img" aria-label="Portrait of massage therapist Elena Brooks" style="left:339px;top:3034px;background:linear-gradient(180deg,#e4e6e8,#9fc3d6)"></div>
<div class="abs team-card" role="img" aria-label="Portrait of chiropractor Daniel Reyes" style="left:607px;top:3034px;background:linear-gradient(180deg,#f1f1f1,#4a4f55)"></div>
<div class="abs team-card" role="img" aria-label="Portrait of physical therapist Sofia Lindqvist" style="left:874px;top:3034px;background:linear-gradient(180deg,#b07a5c,#d8c2b0)"></div>
<div class="abs team-name" style="left:72px;top:3308px">Marcus Hale</div><div class="abs team-role" style="left:72px;top:3334px">Physical Therapist</div>
<div class="abs team-name" style="left:339px;top:3308px">Elena Brooks</div><div class="abs team-role" style="left:339px;top:3334px">Massage Therapist</div>
<div class="abs team-name" style="left:607px;top:3308px">Daniel Reyes</div><div class="abs team-role" style="left:607px;top:3334px">Chiropractor</div>
<div class="abs team-name" style="left:874px;top:3308px">Sofia Lindqvist</div><div class="abs team-role" style="left:874px;top:3334px">Physical Therapist</div>
<div class="abs arrow" style="left:55px;top:3152px;background:#5a6eb5"><svg width="8" height="12"><path d="M7 1 L2 6 L7 11" fill="none" stroke="#fff" stroke-width="2"/></svg></div>
<div class="abs arrow" style="left:1102px;top:3152px;background:var(--green)"><svg width="8" height="12"><path d="M1 1 L6 6 L1 11" fill="none" stroke="#fff" stroke-width="2"/></svg></div>

<!-- Testimonials -->
<div class="abs pill light" style="left:530px;top:3512px;width:140px;height:30px">TESTIMONIAL</div>
<h2 class="abs h-sec" style="left:0;top:3558px;width:1200px;text-align:center">What Our Clients Say</h2>
<div class="abs quote" style="left:70px;top:3650px"><span class="mark">&ldquo;</span><p>Risus commodo viverra manas accumsan las vel facilisis. Vestibum blandit risus ac commodo ornare. Ut et bibendum purus, a facilisis lectus. Nulla varius, dolor vitae varius tempor.</p><div class="who"><div class="av" role="img" aria-label="Client photo"></div><div><b>Lorem ipsum</b><small>Simply Dummy</small></div></div></div>
<div class="abs quote" style="left:435px;top:3650px"><span class="mark">&ldquo;</span><p>Risus commodo viverra manas accumsan las vel facilisis. Vestibum blandit risus ac commodo ornare. Ut et bibendum purus, a facilisis lectus. Nulla varius, dolor vitae varius tempor.</p><div class="who"><div class="av" role="img" aria-label="Client photo"></div><div><b>Lorem ipsum</b><small>Simply Dummy</small></div></div></div>
<div class="abs quote" style="left:802px;top:3650px"><span class="mark">&ldquo;</span><p>Risus commodo viverra manas accumsan las vel facilisis. Vestibum blandit risus ac commodo ornare. Ut et bibendum purus, a facilisis lectus. Nulla varius, dolor vitae varius tempor.</p><div class="who"><div class="av" role="img" aria-label="Client photo"></div><div><b>Lorem ipsum</b><small>Simply Dummy</small></div></div></div>
<div class="abs" style="left:563px;top:3886px;display:flex;gap:20px"><i style="width:11px;height:11px;background:var(--teal);display:block"></i><i style="width:11px;height:11px;background:#ddd;display:block"></i><i style="width:11px;height:11px;background:#ddd;display:block"></i></div>

<!-- Blog -->
<div class="abs pill dark" style="left:540px;top:3986px;width:120px;height:30px">BLOG</div>
<h2 class="abs h-sec" style="left:0;top:4020px;width:1200px;text-align:center;color:#fff">Blog Posts</h2>
<article class="abs blog-card" style="left:72px;top:4097px"><div class="img" role="img" aria-label="Therapist adjusting a patient's neck brace" style="background:linear-gradient(135deg,#e9ecee,#c7b3a6)"></div><div class="abs date"><i></i>Aug 12, 2021</div><h4 class="abs">Vestibulum blandit risus</h4><p class="abs">Ut hendrerit mattis ante a egestas. Ut eget mi mauris. Phasellus metus ipsum, semper at laoreet ut, ullamcorper eget libero.</p><div class="more">Read More <i></i></div></article>
<article class="abs blog-card" style="left:427px;top:4097px"><div class="img" role="img" aria-label="Patient stretching a leg on a treatment table" style="background:linear-gradient(135deg,#dfe7ee,#9fb6cc)"></div><div class="abs date"><i></i>Aug 12, 2021</div><h4 class="abs">Vestibulum blandit risus</h4><p class="abs">Ut hendrerit mattis ante a egestas. Ut eget mi mauris. Phasellus metus ipsum, semper at laoreet ut, ullamcorper eget libero.</p><div class="more">Read More <i></i></div></article>
<article class="abs blog-card" style="left:782px;top:4097px"><div class="img" role="img" aria-label="Gloved hands examining a patient's knee" style="background:linear-gradient(135deg,#f0f0f0,#b9c2c8)"></div><div class="abs date"><i></i>Aug 12, 2021</div><h4 class="abs">Vestibulum blandit risus</h4><p class="abs">Ut hendrerit mattis ante a egestas. Ut eget mi mauris. Phasellus metus ipsum, semper at laoreet ut, ullamcorper eget libero.</p><div class="more">Read More <i></i></div></article>
<div class="abs arrow" style="left:55px;top:4282px;background:#0f6f69"><svg width="8" height="12"><path d="M7 1 L2 6 L7 11" fill="none" stroke="#fff" stroke-width="2"/></svg></div>
<div class="abs arrow" style="left:1102px;top:4282px;background:var(--green)"><svg width="8" height="12"><path d="M1 1 L6 6 L1 11" fill="none" stroke="#fff" stroke-width="2"/></svg></div>

<!-- Footer -->
<div class="abs logo" style="left:72px;top:4700px;font-size:30px"><i></i>KESTROVA</div>
<div class="abs" style="left:72px;top:4800px;font-size:12.5px;line-height:27px;color:var(--muted)">12 Harbour Lane,<br>Sydney, Australia<br>info@kestrovatherapy.com<br>+01 555 204 318</div>
<div class="abs foot-col" style="left:336px;top:4703px"><h5>Quick Links</h5><a>Home</a><a>About Us</a><a>Services</a><a>Blog</a><a>Contact Us</a></div>
<div class="abs foot-col" style="left:521px;top:4703px"><h5>Services</h5><a>Phsical Therapy</a><a>Massage Therapy</a><a>Chirpractic thrapy</a><a>Work Injuries</a><a>Sport Injuries</a></div>
<div class="abs foot-col" style="left:706px;top:4703px;width:420px"><h5>Working Hours</h5>
  <table class="hours" style="width:420px;border-collapse:collapse">
    <tr><td>Monday</td><td>7am – 6pm</td><td>Thursday</td><td style="text-align:right">7am – 6pm</td></tr>
    <tr><td>Tuesday</td><td>7am – 6pm</td><td>Friday</td><td style="text-align:right">7am – 6pm</td></tr>
    <tr><td>Wednesday</td><td>7am – 6pm</td><td>Sat – sun</td><td style="text-align:right">Closed</td></tr>
  </table>
</div>

<div class="abs bottombar">
  <div class="abs" style="left:72px;top:20px">© 2021 <b>Kestrova Physical Therapy &amp; Wellness</b>. All right reserved</div>
  <div class="abs" style="right:72px;top:20px">Social One &nbsp;•&nbsp; Social Two &nbsp;•&nbsp; Video Channel &nbsp;•&nbsp; Photo Feed</div>
</div>

</body>
</html>
```